Shop TalkWave w/Morna Pell (podcast)

Podcast graphic to attract listeners interested in small business tax, bookkeeping and payroll issues. Shop TalkWave w/Morna Pell. Simple, clever and clear. Bold colors that attract attention and make small business owners interested in listening to her and wanting to get to know her. We want to her to appear to be a coach and expert on small business.

Target Market(s)

women and men in small business

Industry/Entity Type

Business Consultant

Font styles to use
Sans Serif

Colors
b260a6
f78f20
32a6d7

Requirements
Must have
• Warm and inviting, positive and uplifting. Promote a personable lady ready and willing to loyally serve her clients and help them succeed in business.
Nice to have
• Clever and smart attracting people that want her business service and advice.
• Emphasize her warmness and open personality.
Should not have
• Nasty or inappropriate,

```html
<!DOCTYPE html>
<html lang="en">
<head>
<meta charset="utf-8">
<title>Shop TalkWave with Morna Pell</title>
<link href="https://fonts.googleapis.com/css2?family=Fredoka:wght@600&family=Kaushan+Script&family=Nunito:wght@700&display=block" rel="stylesheet">
<style>
  :root {
    --plum: #a95fa6;
    --plum-deep: #9a5aa8;
    --sky: #5a8fd0;
    --desk-top: #b07f9e;
    --desk-mid: #a574a8;
    --sheet: #c9a3cf;
    --sheet-line: #b68cbd;
    --bar: #d66a95;
    --bar-soft: #e39a8e;
    --hair: #2a1f24;
    --sweater: #e8922b;
    --navy: #0f3b5c;
    --ice: #d6fbfd;
    --ink: #1a1a1a;
    --white: #ffffff;
  }
  html, body {
    margin: 0;
    padding: 0;
    width: 1200px;
    height: 1200px;
    overflow: hidden;
    background: var(--plum);
  }
  .cover {
    position: relative;
    width: 1200px;
    height: 1200px;
    overflow: hidden;
    background: linear-gradient(100deg, var(--plum) 0%, var(--plum-deep) 55%, var(--sky) 100%);
  }
  .desk-scene {
    position: absolute;
    left: 0;
    top: 0;
    width: 1200px;
    height: 480px;
  }
  .host-portrait {
    position: absolute;
    left: 0;
    top: 0;
    width: 1200px;
    height: 1200px;
  }
  .show-badge {
    position: absolute;
    left: 296px;
    top: 504px;
    display: flex;
    align-items: center;
    gap: 10px;
  }
  .show-badge__dot {
    width: 20px;
    height: 20px;
    border-radius: 50%;
    background: var(--ice);
  }
  .show-badge__name {
    font-family: "Nunito", sans-serif;
    font-weight: 700;
    font-size: 22px;
    letter-spacing: 1px;
    color: var(--ice);
  }
  .show-title {
    position: absolute;
    right: 680px;
    top: 650px;
    margin: 0;
    text-align: right;
    font-family: "Fredoka", sans-serif;
    font-weight: 600;
    font-size: 112px;
    line-height: 1.1;
    color: var(--white);
  }
  .show-title span { display: block; }
  .host-with {
    position: absolute;
    right: 678px;
    top: 912px;
    font-family: "Kaushan Script", cursive;
    font-size: 70px;
    color: var(--ink);
    line-height: 1;
  }
  .host-name {
    position: absolute;
    right: 664px;
    top: 1008px;
    font-family: "Fredoka", sans-serif;
    font-weight: 600;
    font-size: 80px;
    color: var(--white);
    line-height: 1;
  }
</style>
</head>
<body>
  <main class="cover">
    <svg class="desk-scene" viewBox="0 0 1200 480" role="img" aria-label="Photo of a desk with a calculator, pen, glasses and bar chart printouts, tinted purple">
      <defs>
        <linearGradient id="deskTone" x1="0" y1="0" x2="0" y2="1">
          <stop offset="0" stop-color="var(--desk-top)"/>
          <stop offset="0.75" stop-color="var(--desk-mid)"/>
          <stop offset="1" stop-color="var(--plum)" stop-opacity="0"/>
        </linearGradient>
      </defs>
      <rect width="1200" height="480" fill="url(#deskTone)"/>
      <g class="chart-sheet" transform="translate(60 90) rotate(12)" opacity="0.75">
        <rect width="300" height="300" fill="var(--sheet)"/>
        <g fill="var(--bar)">
          <rect x="40" y="150" width="10" height="110"/><rect x="65" y="120" width="10" height="140"/>
          <rect x="90" y="170" width="10" height="90"/><rect x="115" y="100" width="10" height="160"/>
          <rect x="140" y="140" width="10" height="120"/><rect x="165" y="90" width="10" height="170"/>
          <rect x="190" y="130" width="10" height="130"/><rect x="215" y="110" width="10" height="150"/>
          <rect x="240" y="160" width="10" height="100"/>
        </g>
      </g>
      <g class="chart-sheet" transform="translate(360 20) rotate(-8)" opacity="0.6">
        <rect width="180" height="160" fill="var(--sheet)"/>
        <g fill="var(--bar-soft)">
          <rect x="30" y="40" width="8" height="100"/><rect x="50" y="60" width="8" height="80"/>
          <rect x="70" y="30" width="8" height="110"/><rect x="90" y="70" width="8" height="70"/>
          <rect x="110" y="45" width="8" height="95"/><rect x="130" y="55" width="8" height="85"/>
        </g>
      </g>
      <g class="chart-sheet" transform="translate(930 150) rotate(-6)" opacity="0.7">
        <rect width="260" height="290" fill="var(--sheet)"/>
        <g fill="var(--bar)">
          <rect x="40" y="110" width="9" height="140"/><rect x="65" y="90" width="9" height="160"/>
          <rect x="90" y="130" width="9" height="120"/><rect x="115" y="80" width="9" height="170"/>
          <rect x="140" y="120" width="9" height="130"/><rect x="165" y="100" width="9" height="150"/>
          <rect x="190" y="140" width="9" height="110"/>
        </g>
      </g>
    </svg>

    <svg class="host-portrait" viewBox="0 0 1200 1200" role="img" aria-label="Photo of host Morna Pell, dark shoulder-length hair, orange sweater, smiling over her shoulder">
      <defs>
        <linearGradient id="portraitTone" x1="0" y1="0" x2="0" y2="1">
          <stop offset="0" stop-color="var(--hair)"/>
          <stop offset="0.5" stop-color="#5a3a34"/>
          <stop offset="0.68" stop-color="var(--sweater)"/>
          <stop offset="1" stop-color="var(--sweater)"/>
        </linearGradient>
      </defs>
      <path d="M660 1200 C650 1000 630 800 700 560 C750 400 900 320 1010 340 C1090 355 1110 420 1110 520 C1110 640 1060 760 1040 790 C1120 830 1200 880 1200 900 L1200 1200 Z" fill="url(#portraitTone)"/>
    </svg>

    <div class="show-badge">
      <span class="show-badge__dot"></span>
      <span class="show-badge__name">BRIGHTMINDS PODCAST</span>
    </div>

    <h1 class="show-title"><span>Shop</span><span>TalkWave</span></h1>
    <div class="host-with">with</div>
    <div class="host-name">Morna Pell</div>
  </main>
</body>
</html>
```